Travel video blogger needs website design

I need a website designed for my new travel video blog "Roaming Sparrow". I have only just started but need a website that is fairly simple and not too busy. I have a logo which I want on it (I have attached it to this project). I also want a link to all my other social medias on the main page (vidtrekhub, Snapwell and Palnook) and my videos as well. Here is a link to my vidtrekhub page for you to look at: https://www.vidtrekhub.net/channel/QRm4tZ8pWnE2HX57YKccd31v
As I have only just started and I am still trying to find my specific niche, again I need it to be sleek and simple that I can go in and change slightly here and there. I would like these pages on the website: About Me, Videos, Social Media, Blog, Gallery, contact me. for an example I like the look of www.theroamingkinfolk.net website.

I already have the domain and I am with Harborweb with pagecraftr.org. I just want to spend my time getting better and learning about videos then trying to create a website (I am a bit of a perfectionist when I try to do something).

Target Market(s)

Young Adults (majority females) between the ages of 18 and 30 with an interest in travelling.

Industry/Entity Type

Travel Industry

Number of Pages Required

1 page

Colors

Designer to choose colors to be used in the design.

Requirements
Must have
• A like to my Snapwell, Palnook and vidtrekhub channels on the home page
• Must be a nice, simple design
• Must have my logo on the front and name "Roaming Sparrow"
Nice to have
• A nice light, bright coloured theme
Should not have
• A dark coloured theme

```html
<!DOCTYPE html>
<html lang="en">
<head>
<meta charset="utf-8">
<title>Roaming Sparrow – Travel Video Blog</title>
<link rel="stylesheet" href="https://fonts.googleapis.com/css2?family=Raleway:wght@300;400;500;700&family=Lato:wght@400;700&family=Josefin+Sans:wght@700&display=swap">
<style>
:root{
  --ink:#1f1f1f;
  --muted:#777;
  --gold:#d8b07a;
  --gold-line:#c9a26b;
  --white:#ffffff;
  --rule:#e2e2e2;
  --palnook:#2d4f96;
  --vidtrek:#d03a2c;
  --snapwell:#2f6f9a;
}
*{margin:0;padding:0;box-sizing:border-box}
html,body{width:1200px;height:3905px;overflow:hidden;background:var(--white)}
body{position:relative;font-family:"Lato",sans-serif;color:var(--ink)}
.abs{position:absolute}

/* hero */
.hero{left:0;top:0;width:1200px;height:680px}
.hero svg{position:absolute;left:0;top:0}
.brand{left:70px;top:12px;width:136px;text-align:center;color:var(--white)}
.brand-mark{width:46px;height:46px;border:2px solid var(--white);border-radius:50%;margin:0 auto 8px}
.brand-name{font-family:"Raleway",sans-serif;font-weight:700;font-size:13px;letter-spacing:1px;text-transform:uppercase}
.main-nav{left:318px;top:30px;display:flex;gap:26px;font-family:"Raleway",sans-serif;font-size:14px;color:#eee;text-transform:uppercase}
.main-nav .current{color:var(--white);font-weight:700}
.top-social{left:996px;top:20px;display:flex;gap:8px}
.social-dot{border-radius:50%;display:flex;align-items:center;justify-content:center;color:var(--white);font-family:"Lato",sans-serif;font-weight:700}
.top-social .social-dot{width:40px;height:40px;font-size:7px;border:2px solid rgba(255,255,255,.7)}
.hero-title{left:0;top:268px;width:1200px;text-align:center;color:var(--white);font-family:"Raleway",sans-serif;font-weight:400;font-size:48px;line-height:58px;text-transform:uppercase;text-shadow:0 1px 6px rgba(0,0,0,.25)}
.play{left:548px;top:418px;width:104px;height:104px;border-radius:50%;background:rgba(255,255,255,.25);border:3px solid rgba(255,255,255,.5)}
.play::after{content:"";position:absolute;left:25px;top:25px;width:48px;height:48px;border-radius:50%;background:rgba(255,255,255,.35)}
.play svg{position:absolute;left:40px;top:36px;z-index:1}

/* section headings */
.sec-title{left:0;width:1200px;text-align:center;font-family:"Raleway",sans-serif;font-weight:400;font-size:39px}
.sec-title b{font-weight:700}
.sec-sub{left:0;width:1200px;text-align:center;font-size:13px;color:var(--muted)}

/* about */
.about-bg{left:0;top:1093px;width:1200px;height:392px;background:
  radial-gradient(ellipse 300px 260px at 80px 330px,#bdbdbd,rgba(190,190,190,0) 70%),
  radial-gradient(ellipse 320px 260px at 1130px 320px,#c4c4c4,rgba(196,196,196,0) 70%),
  linear-gradient(180deg,#ffffff 0%,#f1f1f1 50%,#dedede 100%)}
.intro-video{left:234px;top:841px;width:730px;height:336px;background:
  radial-gradient(ellipse 200px 220px at 410px 200px,#e2c49c,rgba(226,196,156,0) 75%),
  linear-gradient(90deg,#2f2f31 0%,#4a4846 30%,#8d7c68 55%,#cfc6bb 80%,#ece8e2 100%)}
.about-heading{left:250px;top:1214px;font-family:"Raleway",sans-serif;font-size:38px}
.about-heading b{font-weight:700}
.about-text{left:518px;top:1212px;width:450px;font-size:14px;line-height:22px;color:#444}
.about-text p{margin-bottom:10px}

/* stories */
.story{width:320px;text-align:center}
.story-photo{width:302px;height:229px;margin:0 auto;overflow:hidden;position:relative}
.story-photo span{position:absolute;left:0;top:0;width:302px;height:302px;border-radius:50%}
.story-rule{height:1px;background:var(--rule);width:320px}
.story-kicker{margin-top:22px;font-size:15px;color:#333;text-transform:uppercase}
.story-title{margin-top:4px;font-family:"Josefin Sans",sans-serif;font-weight:700;font-size:15px;letter-spacing:2px;text-transform:uppercase;color:#222}
.btn{left:463px;top:2746px;width:274px;height:52px;border-radius:26px;background:var(--gold);color:var(--white);font-family:"Raleway",sans-serif;font-size:17px;text-transform:uppercase;display:flex;align-items:center;justify-content:center}

/* gallery */
.gal-side{top:3001px;height:313px;width:318px}
.gal-frame{left:315px;top:2962px;width:570px;height:396px;background:#000}
.gal-photo{left:367px;top:3027px;width:466px;height:258px;background:
  radial-gradient(ellipse 150px 170px at 190px 120px,#e6c9a4,rgba(230,201,164,0) 75%),
  linear-gradient(90deg,#9bb0c2 0%,#c9d3da 40%,#dcd2c4 70%,#eef2f5 100%)}
.gal-caption{left:400px;top:3232px;font-family:"Raleway",sans-serif;font-style:italic;font-size:38px;color:var(--white);opacity:.9}
.gal-nav{top:3138px;font-family:"Raleway",sans-serif;font-size:24px;color:#222;display:flex;align-items:center;gap:8px}

/* social */
.social-row{left:495px;top:3488px;display:flex;gap:11px}
.social-row .social-dot{width:62px;height:62px;font-size:10px}

/* footer */
.footer{left:0;top:3620px;width:1200px;height:285px}
.footer svg{position:absolute;left:0;top:0}
.foot-brand{left:70px;top:3722px;width:170px;text-align:center;color:var(--white)}
.foot-brand .brand-mark{width:60px;height:60px}
.foot-brand .brand-name{font-size:17px}
.foot-nav{right:76px;top:3765px;font-size:14px;color:#f2f2f2;display:flex;gap:12px}
.foot-nav span.sep{color:#ccc}
.copyright{right:76px;top:3797px;font-size:14px;color:#eee}
</style>
</head>
<body>

<header class="hero abs">
  <svg width="1200" height="680" viewBox="0 0 1200 680" role="img" aria-label="Travel photo of a young woman on a palm-lined sandy coast at dusk">
    <defs>
      <linearGradient id="heroFill" x1="0" y1="0" x2="1" y2="1">
        <stop offset="0" stop-color="#59636f"/>
        <stop offset="0.45" stop-color="#6e7a86"/>
        <stop offset="0.75" stop-color="#8d7c68"/>
        <stop offset="1" stop-color="#b89a74"/>
      </linearGradient>
      <radialGradient id="heroGlow" cx="0.2" cy="0.35" r="0.35">
        <stop offset="0" stop-color="#c8b8a6" stop-opacity="0.55"/>
        <stop offset="1" stop-color="#c8b8a6" stop-opacity="0"/>
      </radialGradient>
      <linearGradient id="heroShade" x1="0" y1="0" x2="0" y2="1">
        <stop offset="0" stop-color="#1e242b" stop-opacity="0.45"/>
        <stop offset="0.35" stop-color="#1e242b" stop-opacity="0.1"/>
        <stop offset="1" stop-color="#1e242b" stop-opacity="0.2"/>
      </linearGradient>
    </defs>
    <path d="M0 0H1200V585Q600 690 0 585Z" fill="url(#heroFill)"/>
    <path d="M0 0H1200V585Q600 690 0 585Z" fill="url(#heroGlow)"/>
    <path d="M0 0H1200V585Q600 690 0 585Z" fill="url(#heroShade)"/>
    <path d="M0 590Q600 700 1200 590" fill="none" stroke="var(--gold-line)" stroke-width="6"/>
  </svg>
  <div class="brand abs">
    <div class="brand-mark"></div>
    <div class="brand-name">Roaming Sparrow</div>
  </div>
  <nav class="main-nav abs">
    <span class="current">Home</span><span>About Me</span><span>Social Media</span><span>Blog</span><span>Gallery</span><span>Contact Me</span>
  </nav>
  <div class="top-social abs">
    <span class="social-dot" style="background:var(--palnook)">Palnook</span>
    <span class="social-dot" style="background:var(--vidtrek)">VidTrek</span>
    <span class="social-dot" style="background:var(--snapwell)">Snapwell</span>
  </div>
  <h1 class="hero-title abs">Discover the art of traveling<br>anywhere you want</h1>
  <div class="play abs"><svg width="26" height="32" viewBox="0 0 26 32"><path d="M0 0L26 16L0 32Z" fill="#fff"/></svg></div>
</header>

<h2 class="sec-title abs" style="top:740px">Welcome To <b>Roaming Sparrow</b></h2>
<p class="sec-sub abs" style="top:800px">Lorem Ipsum is simply dummy text of the printing</p>

<div class="about-bg abs" role="img" aria-label="Faded grey mountain landscape"></div>
<div class="intro-video abs" role="img" aria-label="Video still of the host talking on a sofa"></div>
<h2 class="about-heading abs">About <b>Me</b></h2>
<div class="about-text abs">
  <p>Welcome to my channel Roaming Sparrow!</p>
  <p>Every week I post a new video of an adventure I've been on this week. All leading up to the 17th April when I step on a plane for a one way adventure of a lifetime!</p>
  <p>So stay tuned each week for more of the videos you love and make sure to subscribe!</p>
</div>

<h2 class="sec-title abs" style="top:1542px">We have so many Stories.<b>To Tell You</b></h2>
<p class="sec-sub abs" style="top:1604px">Lorem Ipsum is simply dummy text of the printing and typesetting industry.</p>

<div class="story abs" style="left:77px;top:1676px"><div class="story-photo"><span role="img" aria-label="Travel video still of children by a red stage curtain" style="background:linear-gradient(90deg,#3a3f4a 0%,#7b2a2a 45%,#b8302e 70%,#9a8c86 100%)"></span></div><div class="story-rule"></div><div class="story-kicker">Lorem Ipsum</div><div class="story-title">Lorem is simply text</div></div>
<div class="story abs" style="left:439px;top:1676px"><div class="story-photo"><span role="img" aria-label="Ocean waves against a headland" style="background:linear-gradient(180deg,#c3ccd3 0%,#a9b5bd 50%,#5f7782 70%,#8a8e88 100%)"></span></div><div class="story-rule"></div><div class="story-kicker">Lorem Ipsum</div><div class="story-title">Lorem is simply text</div></div>
<div class="story abs" style="left:803px;top:1676px"><div class="story-photo"><span role="img" aria-label="Performer on a colourful stage" style="background:radial-gradient(circle at 50% 65%,#d8468f,rgba(216,70,143,0) 45%),linear-gradient(160deg,#2a3aa8,#4a5ad0 55%,#6a4ab8)"></span></div><div class="story-rule"></div><div class="story-kicker">Lorem Ipsum</div><div class="story-title">Lorem is simply text</div></div>

<div class="story abs" style="left:77px;top:2030px"><div class="story-photo"><span role="img" aria-label="Wide sandy beach under blue sky" style="background:linear-gradient(180deg,#3f78bd 0%,#8fb3d6 55%,#b4a286 70%,#9c8a70 100%)"></span></div><div class="story-rule"></div><div class="story-kicker">Lorem Ipsum</div><div class="story-title">Lorem is simply text</div></div>
<div class="story abs" style="left:439px;top:2030px"><div class="story-photo"><span role="img" aria-label="Tropical bay with green hills" style="background:linear-gradient(180deg,#a8c8e2 0%,#5c9346 40%,#4f8a8a 62%,#e2cf94 80%)"></span></div><div class="story-rule"></div><div class="story-kicker">Lorem Ipsum</div><div class="story-title">Lorem is simply text</div></div>
<div class="story abs" style="left:803px;top:2030px"><div class="story-photo"><span role="img" aria-label="Coastline with dune grass" style="background:linear-gradient(135deg,#e6dfcf 0%,#5a86a6 40%,#dcd6c8 65%,#b79a6a 100%)"></span></div><div class="story-rule"></div><div class="story-kicker">Lorem Ipsum</div><div class="story-title">Lorem is simply text</div></div>

<div class="story abs" style="left:77px;top:2387px"><div class="story-photo"><span role="img" aria-label="Hot air balloons over temples at sunrise" style="background:linear-gradient(180deg,#f0d2b8 0%,#e0a880 45%,#b4704a 70%,#6a4430 100%)"></span></div><div class="story-rule"></div><div class="story-kicker">Lorem Ipsum</div><div class="story-title">Lorem is simply text</div></div>
<div class="story abs" style="left:439px;top:2387px"><div class="story-photo"><span role="img" aria-label="Boat ride through a green river forest" style="background:linear-gradient(180deg,#8aa462 0%,#56743e 45%,#c8ad78 70%,#8a6c44 100%)"></span></div><div class="story-rule"></div><div class="story-kicker">Lorem Ipsum</div><div class="story-title">Lorem is simply text</div></div>
<div class="story abs" style="left:803px;top:2387px"><div class="story-photo"><span role="img" aria-label="Traveller sitting by a mountain lake" style="background:linear-gradient(180deg,#a8cdea 0%,#e8eef2 30%,#5b8a6a 50%,#3f7fb0 75%,#c8c2b6 100%)"></span></div><div class="story-rule"></div><div class="story-kicker">Lorem Ipsum</div><div class="story-title">Lorem is simply text</div></div>

<div class="btn abs">Explore more videos</div>

<h2 class="sec-title abs" style="top:2856px">Our <b>Gallery</b></h2>
<p class="sec-sub abs" style="top:2916px">Lorem Ipsum is simply dummy text of the printing and typesetting industry.</p>

<div class="gal-side abs" role="img" aria-label="Greyed video still, previous item" style="left:0;background:radial-gradient(ellipse 110px 140px at 150px 170px,#c9c9c9,rgba(201,201,201,0) 75%),linear-gradient(90deg,#8a8a8a,#b8b8b8 50%,#e2e2e2)"></div>
<div class="gal-side abs" role="img" aria-label="Greyed video still, next item" style="left:882px;background:radial-gradient(ellipse 110px 140px at 160px 170px,#c9c9c9,rgba(201,201,201,0) 75%),linear-gradient(90deg,#e2e2e2,#b8b8b8 50%,#8a8a8a)"></div>
<div class="gal-frame abs"></div>
<div class="gal-photo abs" role="img" aria-label="Video still of the host outdoors"></div>
<div class="gal-caption abs">What I did this week...</div>
<div class="gal-nav abs" style="left:72px"><svg width="46" height="14" viewBox="0 0 46 14"><path d="M46 7H2M9 1L2 7L9 13" fill="none" stroke="#222" stroke-width="1.6"/></svg>Prev</div>
<div class="gal-nav abs" style="left:1026px">Next<svg width="46" height="14" viewBox="0 0 46 14"><path d="M0 7H44M37 1L44 7L37 13" fill="none" stroke="#222" stroke-width="1.6"/></svg></div>

<h2 class="sec-title abs" style="top:3416px">We Are <b>Social</b></h2>
<div class="social-row abs">
  <span class="social-dot" style="background:var(--palnook)">Palnook</span>
  <span class="social-dot" style="background:var(--vidtrek)">VidTrekHub</span>
  <span class="social-dot" style="background:var(--snapwell)">Snapwell</span>
</div>

<footer class="footer abs">
  <svg width="1200" height="285" viewBox="0 0 1200 285" role="img" aria-label="Misty mountain ridge landscape at dusk">
    <defs>
      <linearGradient id="footFill" x1="0" y1="0" x2="0" y2="1">
        <stop offset="0" stop-color="#7d8994"/>
        <stop offset="0.45" stop-color="#5c6670"/>
        <stop offset="1" stop-color="#3c4249"/>
      </linearGradient>
      <radialGradient id="footGlow" cx="0.55" cy="0.35" r="0.45">
        <stop offset="0" stop-color="#a8957a" stop-opacity="0.5"/>
        <stop offset="1" stop-color="#a8957a" stop-opacity="0"/>
      </radialGradient>
    </defs>
    <path d="M0 45Q600 -25 1200 45V285H0Z" fill="url(#footFill)"/>
    <path d="M0 45Q600 -25 1200 45V285H0Z" fill="url(#footGlow)"/>
    <path d="M0 42Q600 -28 1200 42" fill="none" stroke="var(--gold-line)" stroke-width="6"/>
    <rect x="0" y="279" width="1200" height="6" fill="var(--gold-line)"/>
  </svg>
</footer>
<div class="foot-brand abs">
  <div class="brand-mark"></div>
  <div class="brand-name">Roaming Sparrow</div>
</div>
<nav class="foot-nav abs"><span>Home</span><span class="sep">|</span><span>About Me</span><span class="sep">|</span><span>Videos</span><span class="sep">|</span><span>Social Media</span><span class="sep">|</span><span>Blog</span><span class="sep">|</span><span>Gallery</span><span class="sep">|</span><span>Contact Me</span></nav>
<p class="copyright abs">©Roaming Sparrow - 2018 All Right Reserved.</p>

</body>
</html>
```